Accountancy firm needs clean and simple website and optional logo

We need a logo and basic wordpress website design for a Sydney based accountancy firm.
We need a clean and simple logo and website, based on the accounting/finance/tax industry. Simple, credible and official colors.
The logo is expected to be so simple that we have combined into the one job.
If you submit a logo design and we choose it along with someone else's website design you will be paid a bonus of $60. The website design will still win the competition as per normal.
Current website is old and terrible but gives you an idea of the sitemap (super simple) and what they do: www.brookfiscal.com.au
We want original different to normal template looking designs.
We like videos, and like http://www.whitfords.com.au/
Feel free to go to vidhaven and use some videos from there.
We are based in Sydney Australia and in the field of taxation and accounting
We want a clean, formal, credible site, limited pages.
The project is guaranteed, so go for it.
Brook & Associates
1 page

```html
<!DOCTYPE html>
<html lang="en">
<head>
<meta charset="utf-8">
<title>Brook &amp; Associates — Tax Accounts</title>
<link href="https://fonts.googleapis.com/css2?family=Questrial&family=Arimo:ital,wght@0,400;0,700;1,400&family=Raleway:wght@500;600&display=swap" rel="stylesheet">
<style>
  :root {
    --teal: #0c93ad;
    --teal-dark: #08839b;
    --green: #7ab51d;
    --ink: #1d1d1d;
    --text: #555;
    --muted: #8a8a8a;
    --grey-band: #e1e1e1;
    --white: #ffffff;
    --hero-light: #dbe6f2;
    --hero-mid: #9fb8d6;
    --hero-deep: #5f82b1;
    --video-deep: #0a1f5c;
    --video-mid: #2450b8;
    --social: #cfcfcf;
  }
  * { box-sizing: border-box; margin: 0; padding: 0; }
  html, body { width: 969px; height: 1200px; overflow: hidden; background: var(--white); }
  body { position: relative; font-family: "Arimo", Arial, sans-serif; color: var(--text); }
  .abs { position: absolute; }

  .top-rule { left: 0; top: 0; width: 969px; height: 11px; background: var(--teal); z-index: 3; }
  .hero { left: 0; top: 0; width: 969px; height: 375px;
    background: linear-gradient(160deg, var(--hero-mid) 0%, var(--hero-light) 35%, var(--hero-light) 55%, var(--hero-mid) 80%, var(--hero-deep) 100%); }
  .masthead { left: 0; top: 11px; width: 969px; height: 107px; background: rgba(255,255,255,0.72);
    border-bottom: 1px solid rgba(120,140,170,0.5); z-index: 2; }
  .brand-mark { left: 68px; top: 21px; width: 43px; height: 41px; border-radius: 6px; background: var(--teal); }
  .brand-name { left: 32px; top: 74px; font-family: "Questrial", sans-serif; font-weight: 400; font-size: 11.5px;
    letter-spacing: 0.3px; color: var(--ink); white-space: nowrap; }
  .brand-tag { left: 32px; top: 88px; width: 112px; text-align: right; font-family: "Questrial", sans-serif;
    font-size: 8px; color: var(--teal); }
  .nav { top: 70px; font-family: "Questrial", sans-serif; font-size: 16px; color: var(--ink); }
  .nav-home { left: 686px; } .nav-about { left: 765px; } .nav-contact { left: 843px; }

  .service { top: 410px; width: 240px; text-align: center; }
  .service svg { display: block; margin: 0 auto; }
  .service h3 { margin-top: 17px; font-family: "Questrial", sans-serif; font-weight: 400; font-size: 12.5px; color: var(--ink); letter-spacing: 0.2px; }
  .service p { margin-top: 10px; font-size: 9.5px; line-height: 16px; color: var(--muted); }

  .notify-band { left: 0; top: 578px; width: 969px; height: 258px; background: var(--grey-band); }
  .notify-title { left: 126px; top: 610px; font-family: "Raleway", sans-serif; font-weight: 600; font-size: 14px; color: var(--ink); }
  .notify-copy { left: 126px; top: 638px; width: 330px; font-size: 9.5px; line-height: 16px; color: var(--muted); }
  .email-field { left: 126px; top: 714px; width: 186px; height: 34px; background: var(--white); border: 1px solid #c9c9c9;
    border-right: none; border-radius: 8px 0 0 8px; font-size: 10.5px; color: #8d8d8d; padding: 10px 0 0 14px; }
  .notify-btn { left: 311px; top: 714px; width: 85px; height: 34px; background: var(--teal); color: var(--white);
    border-radius: 0 8px 8px 0; font-family: "Raleway", sans-serif; font-weight: 600; font-size: 14px; text-align: center; line-height: 34px; }
  .video { left: 538px; top: 614px; width: 304px; height: 186px; border-radius: 4px; overflow: hidden;
    background: radial-gradient(ellipse at 65% 40%, var(--video-mid) 0%, #17368f 45%, var(--video-deep) 100%); }

  .quote { left: 0; top: 868px; width: 969px; text-align: center; font-style: italic; font-size: 11px; line-height: 18px; color: var(--muted); }
  .quote-name { left: 0; top: 914px; width: 969px; text-align: center; font-weight: 700; font-size: 10.5px; color: var(--ink); }
  .client-strip { left: 138px; top: 943px; width: 685px; height: 31px;
    background: linear-gradient(90deg, rgba(200,190,180,0.3) 0%, #b99a84 8%, #8c7a6c 30%, #c6a58d 50%, #7d6a5d 70%, #b69c88 92%, rgba(200,190,180,0.3) 100%); }

  .touch-title { left: 0; top: 1006px; width: 969px; text-align: center; font-family: "Questrial", sans-serif; font-size: 15px; color: var(--ink); }
  .touch-copy { left: 0; top: 1034px; width: 969px; text-align: center; font-size: 9.5px; color: var(--muted); }
  .socials { left: 408px; top: 1062px; }

  .footer { left: 0; top: 1119px; width: 969px; height: 81px; background: var(--grey-band); }
  .footer-links { left: 0; top: 1153px; width: 969px; display: flex; justify-content: center; gap: 21px;
    font-family: "Questrial", sans-serif; font-size: 10px; color: #444; }
</style>
</head>
<body>
  <div class="abs top-rule"></div>
  <div class="abs hero" role="img" aria-label="Photo of a calculator, pen and a financial chart printout in soft blue tones"></div>

  <header class="abs masthead">
    <div class="abs brand-mark"></div>
    <div class="abs brand-name">BROOK &amp; ASSOCIATES</div>
    <div class="abs brand-tag">TAX ACCOUNTS</div>
    <nav>
      <span class="abs nav nav-home">HOME</span>
      <span class="abs nav nav-about">ABOUT</span>
      <span class="abs nav nav-contact">CONTACT</span>
    </nav>
  </header>

  <section class="services">
    <div class="abs service" style="left:102px">
      <svg width="60" height="60" viewBox="0 0 60 60"><circle cx="30" cy="30" r="30" fill="var(--teal)"/>
        <rect x="16" y="16" width="28" height="28" rx="4" fill="var(--green)"/>
        <rect x="20" y="19" width="20" height="5" fill="#fff"/>
        <g fill="#fff"><rect x="20" y="27" width="4" height="3"/><rect x="26" y="27" width="4" height="3"/><rect x="32" y="27" width="4" height="3"/><rect x="37" y="27" width="3" height="3"/>
        <rect x="20" y="32" width="4" height="3"/><rect x="26" y="32" width="4" height="3"/><rect x="32" y="32" width="4" height="3"/><rect x="37" y="32" width="3" height="3"/>
        <rect x="20" y="37" width="4" height="3"/><rect x="26" y="37" width="4" height="3"/><rect x="32" y="37" width="4" height="3"/><rect x="37" y="37" width="3" height="3"/></g>
      </svg>
      <h3>TAXES</h3>
      <p>Lorem ipsum dolor sit amet, consectetur adipiscing<br>elit. Proin quis justo in tellus aliquam posuere.</p>
    </div>
    <div class="abs service" style="left:362px">
      <svg width="60" height="60" viewBox="0 0 60 60"><circle cx="30" cy="30" r="30" fill="var(--teal)"/>
        <rect x="16" y="16" width="28" height="28" rx="4" fill="var(--green)"/>
        <g stroke="#fff" stroke-width="2"><line x1="20" y1="22" x2="40" y2="22"/><line x1="20" y1="27" x2="40" y2="27"/><line x1="20" y1="32" x2="40" y2="32"/><line x1="20" y1="37" x2="40" y2="37"/></g>
      </svg>
      <h3>DONEC ALIQUAM</h3>
      <p>Lorem ipsum dolor sit amet, consectetur<br>adipiscing elit. Suspendisse fringilla fringilla.</p>
    </div>
    <div class="abs service" style="left:623px">
      <svg width="60" height="60" viewBox="0 0 60 60"><circle cx="30" cy="30" r="30" fill="var(--teal)"/>
        <rect x="16" y="16" width="28" height="28" rx="4" fill="var(--green)"/>
        <polyline points="19,38 26,31 30,34 39,24" fill="none" stroke="#fff" stroke-width="2.5"/>
        <polygon points="35,23 41,22 40,28" fill="#fff"/>
      </svg>
      <h3>CURABITUR ALIQUET</h3>
      <p>Lorem ipsum dolor sit amet, consectetur<br>adipiscing elit. Suspendisse fringilla fringilla.</p>
    </div>
  </section>

  <section>
    <div class="abs notify-band"></div>
    <h2 class="abs notify-title">Get Notified Of Any Updates!</h2>
    <p class="abs notify-copy">Lorem ipsum dolor sit amet, consectetur adipiscing elit. Suspendisse fringilla fringilla nisl congue congue. Maecenas nec condimentum libero, at elementum mauris. Phasellus eget nisi dapibus, ultricies nisl at, hendrerit risusuis ornare luctus id sollicitudin ante lobortis at.</p>
    <div class="abs email-field">Email Address</div>
    <div class="abs notify-btn">Notify</div>
    <div class="abs video" role="img" aria-label="Video still of glowing stock price figures on a blue screen">
      <svg class="abs" style="left:0;top:0" width="304" height="186" viewBox="0 0 304 186">
        <rect x="12" y="148" width="280" height="28" rx="3" fill="rgba(20,20,30,0.55)"/>
        <rect x="12" y="148" width="42" height="28" rx="3" fill="#1b1b1f"/>
        <polygon points="29,156 29,168 39,162" fill="#fff"/>
        <rect x="73" y="160" width="155" height="5" rx="2" fill="#2a2a35" stroke="#4d5a70" stroke-width="0.5"/>
        <rect x="73" y="160" width="100" height="5" rx="2" fill="#2aa9e0"/>
        <rect x="162" y="150" width="22" height="8" rx="1" fill="#eee"/>
        <text x="173" y="156.5" font-size="5.5" text-anchor="middle" fill="#333" font-family="Arimo, sans-serif">00:34</text>
        <g fill="#2aa9e0"><rect x="234" y="159" width="2" height="7"/><rect x="238" y="159" width="2" height="7"/><rect x="242" y="159" width="2" height="7"/><rect x="246" y="159" width="2" height="7"/><rect x="250" y="159" width="2" height="7"/></g>
        <text x="262" y="165.5" font-size="6.5" font-weight="700" fill="#2aa9e0" font-family="Arimo, sans-serif">HD</text>
        <g stroke="#fff" stroke-width="1.3"><line x1="279" y1="158" x2="286" y2="166"/><line x1="286" y1="158" x2="279" y2="166"/></g>
      </svg>
    </div>
  </section>

  <section>
    <p class="abs quote">“Lorem ipsum dolor sit amet, consectetur adipiscing elit. Mauris interdum velit vitae nulla molestie eu<br>commodo nulla dapib us. Donec id sollicitudin urna. Integer at dui ac leo fermentum varius eleifend ut.”</p>
    <p class="abs quote-name">Clara Hollis</p>
    <div class="abs client-strip" role="img" aria-label="Row of small client portrait photos"></div>
  </section>

  <section>
    <h2 class="abs touch-title">Get in Touch</h2>
    <p class="abs touch-copy">Lorem ipsum dolor sit amet, consectetur adipiscing elit suspendisse.</p>
    <svg class="abs socials" width="154" height="20" viewBox="0 0 154 20" aria-label="Social links">
      <circle cx="9" cy="10" r="9" fill="var(--social)"/>
      <circle cx="36" cy="10" r="9" fill="var(--teal)"/>
      <circle cx="62" cy="10" r="9" fill="var(--social)"/>
      <circle cx="89" cy="10" r="9" fill="var(--social)"/>
      <circle cx="115" cy="10" r="9" fill="var(--social)"/>
      <circle cx="142" cy="10" r="9" fill="var(--social)"/>
    </svg>
  </section>

  <footer>
    <div class="abs footer"></div>
    <nav class="abs footer-links">
      <span>Contact</span><span>Ipsum</span><span>Press</span><span>Email</span><span>Support</span><span>Privacy Policy</span>
    </nav>
  </footer>
</body>
</html>
```